COMPANY SIGN

I am in the process of ordering new company For Sale signs and stationary (business cards, envelopes, letterheads, and labels). I need a new design with my existing company logo. The TWO MOST IMPORTANT PROJECTS I need right now is the new design for the company sign and business cards. I've uploaded a .jpg file of my company logo.

I like the design to be eye catching and the background color of the company sign to be soothing to the eyes. Perhaps, using one of the color on the leaves of the logo or any other color that the designer think will go well with the logo. My favorite colors are teal or light olive color but don't let that affect your creativity.

Industry/Entity Type

Business

Requirements
Should not have
• Please don't use "Times New Roman" fonts or fonts that is hard to read.

```html
<!DOCTYPE html>
<html lang="en">
<head>
<meta charset="utf-8">
<title>Maplewood House Walk – Business Card</title>
<link rel="stylesheet" href="https://fonts.googleapis.com/css2?family=Open+Sans:wght@300;700&display=swap">
<style>
  :root {
    --page: #ffffff;
    --ink: #000000;
    --card: #23e1e1;
    --glow: #ffffff;
    --text: #ffffff;
    --yellow: #e5df06;
    --olive: #bdc43f;
    --blue: #78b5d6;
    --orange: #ec8a32;
  }
  * { margin: 0; padding: 0; box-sizing: border-box; }
  html, body {
    width: 932px;
    height: 1200px;
    overflow: hidden;
    background: var(--page);
    font-family: "Open Sans", Arial, sans-serif;
  }
  .sheet { position: relative; width: 932px; height: 1200px; }

  .side-label {
    position: absolute;
    left: 0;
    width: 932px;
    text-align: center;
    font-weight: 700;
    font-size: 46px;
    line-height: 1;
    color: var(--ink);
  }
  .side-label--front { top: 6px; }
  .side-label--back { top: 640px; }

  .card {
    position: absolute;
    left: 81px;
    width: 770px;
    color: var(--text);
    font-weight: 300;
  }
  .card--front { top: 81px; }
  .card--back { top: 712px; }

  .card__face {
    position: relative;
    height: 423px;
    background: var(--card);
    overflow: hidden;
  }
  .card--back .card__face { height: 415px; }
  .card--front .card__face {
    background:
      radial-gradient(ellipse 300px 220px at 50% 0%, rgba(255,255,255,0.85), rgba(255,255,255,0) 100%),
      var(--card);
  }

  .stripe { display: flex; height: 16px; }
  .stripe span { width: 83px; flex: none; }
  .stripe span:last-child { width: 23px; }
  .stripe .y { background: var(--yellow); }
  .stripe .o { background: var(--olive); }
  .stripe .b { background: var(--blue); }
  .stripe .r { background: var(--orange); }

  .brand { position: absolute; left: 0; width: 100%; text-align: center; }
  .brand__mark {
    display: block;
    margin: 0 auto;
    border-radius: 50%;
    background: var(--olive);
  }
  .brand__name { display: block; line-height: 1; }
  .brand__tagline { display: block; line-height: 1; letter-spacing: 0.32em; }

  .card--front .brand { top: 82px; }
  .card--front .brand__mark { width: 110px; height: 110px; margin-bottom: 38px; }
  .card--front .brand__name { font-size: 96px; }
  .card--front .brand__tagline { font-size: 32px; margin-top: 8px; }

  .card--back .brand { top: 38px; }
  .card--back .brand__mark { width: 62px; height: 62px; margin-bottom: 28px; }
  .card--back .brand__name { font-size: 60px; }
  .card--back .brand__tagline { font-size: 20px; margin-top: 6px; }

  .holder { position: absolute; left: 16px; top: 278px; }
  .holder__name { font-size: 36px; line-height: 1.1; }
  .holder__role { font-size: 14px; margin-left: 8px; }

  .contact {
    position: absolute;
    right: 25px;
    top: 282px;
    text-align: right;
    font-size: 25px;
    line-height: 36px;
    list-style: none;
  }
</style>
</head>
<body>
<main class="sheet">
  <h2 class="side-label side-label--front">FRONT</h2>
  <section class="card card--front" aria-label="Business card front">
    <div class="card__face">
      <div class="brand">
        <span class="brand__mark"></span>
        <span class="brand__name">Maplewood</span>
        <span class="brand__tagline">HOUSE WALK</span>
      </div>
    </div>
    <div class="stripe"><span class="y"></span><span class="o"></span><span class="b"></span><span class="r"></span><span class="y"></span><span class="o"></span><span class="b"></span><span class="r"></span><span class="y"></span><span class="o"></span></div>
  </section>

  <h2 class="side-label side-label--back">BACK</h2>
  <section class="card card--back" aria-label="Business card back">
    <div class="card__face">
      <div class="brand">
        <span class="brand__mark"></span>
        <span class="brand__name">Maplewood</span>
        <span class="brand__tagline">HOUSE WALK</span>
      </div>
      <div class="holder">
        <p class="holder__name">Your Name Here</p>
        <p class="holder__role">position</p>
      </div>
      <ul class="contact">
        <li>1011 Street, Homeland</li>
        <li>123-456-789</li>
        <li>your@email.com</li>
      </ul>
    </div>
    <div class="stripe"><span class="y"></span><span class="o"></span><span class="b"></span><span class="r"></span><span class="y"></span><span class="o"></span><span class="b"></span><span class="r"></span><span class="y"></span><span class="o"></span></div>
  </section>
</main>
</body>
</html>
```